Larkhollow Fitness

Personal training company specializing in fat burn and toning in minimal time with maximal results.

I am looking to launch my company and i am looking to target a specific market women between the ages of 30 to 50 who are stay at home mums and business professionals looking to kick start there health and fitness goals. We are based in the Epsom Ewell area in Surrey. Our initial product are the 30 minute 1to1 sessions. Colors of my company brand are cyan and black. The final design should communicate "solid results minimal time" and should have a tear off tab so i can capture data.

Target Market(s)

women between 30-50 yrs old stay at home mums or buisness proffesionals

Industry/Entity Type

Training

Requirements
Must have
• Tear off section to capture details of potential clients
Should not have
• no money bags
no cheesey sayings

```html
<!DOCTYPE html>
<html lang="en">
<head>
<meta charset="utf-8">
<title>Larkhollow Personal Training – Kickstart Flyer</title>
<link rel="stylesheet" href="https://fonts.googleapis.com/css2?family=Anton&family=Oswald:wght@400;600&family=Open+Sans:wght@400;600&family=Arimo:wght@700&display=swap">
<style>
  :root {
    --stage: #16201f;
    --paper: #ececec;
    --paper-light: #f4f4f4;
    --cyan: #1b98c8;
    --cyan-deep: #1589b6;
    --ink: #111111;
    --muted: #666666;
    --red: #e0201f;
    --white: #ffffff;
    --skin: #e7b99c;
    --top-pink: #d9468e;
  }
  * { box-sizing: border-box; margin: 0; padding: 0; }
  html, body {
    width: 1200px; height: 990px; overflow: hidden;
    background: var(--stage);
  }
  .flyer {
    position: absolute; left: 40px; top: 68px;
    width: 1120px; height: 854px;
    background: linear-gradient(180deg, var(--paper-light), var(--paper));
    overflow: hidden;
  }
  .trainer-photo {
    position: absolute; left: 0; top: 0; width: 420px; height: 854px;
    background: linear-gradient(180deg, #efe9e2 0%, var(--skin) 35%, var(--top-pink) 55%, var(--skin) 75%, #4c4a52 100%);
  }
  .slogan-art {
    position: absolute; left: 207px; top: 35px; width: 332px; height: 197px;
    background: #dfe9ec; border-radius: 14px;
  }
  .brand-name {
    position: absolute; left: 555px; top: 18px; width: 540px;
    text-align: center;
    font-family: "Anton", sans-serif; font-weight: 400; font-size: 100px; line-height: 150px;
    color: var(--cyan);
  }
  .brand-tagline {
    position: absolute; left: 555px; top: 196px; width: 540px;
    text-align: center;
    font-family: "Oswald", sans-serif; font-weight: 400; font-size: 50px; line-height: 1.1;
    color: var(--ink);
  }
  .headline-band {
    position: absolute; left: 232px; top: 267px; width: 888px; height: 202px;
    background: linear-gradient(90deg, rgba(27,152,200,0) 0%, var(--cyan) 22%, var(--cyan-deep) 100%);
    display: flex; flex-direction: column; justify-content: center; align-items: center;
    padding-left: 180px; padding-right: 20px; gap: 18px;
  }
  .headline-band p {
    font-family: "Oswald", sans-serif; font-weight: 600; font-size: 30px; line-height: 1.2;
    color: var(--white); text-transform: uppercase; white-space: nowrap;
  }
  .offer-title {
    position: absolute; left: 420px; top: 494px; width: 690px; text-align: center;
    font-family: "Arimo", sans-serif; font-weight: 700; font-size: 48px; line-height: 1.1;
    color: var(--red);
  }
  .offer-list {
    position: absolute; left: 420px; top: 552px; width: 690px;
    list-style: none;
  }
  .offer-list li {
    height: 36px; margin-bottom: 5px;
    background: var(--white); border-radius: 10px;
    padding: 0 14px;
    font-family: "Open Sans", sans-serif; font-size: 20px; line-height: 36px;
    color: var(--ink); white-space: nowrap;
  }
  .tear-off {
    position: absolute; left: 420px; top: 768px; width: 690px; height: 78px;
    border-top: 2px dashed var(--muted);
    padding-top: 10px;
  }
  .tear-off-title {
    font-family: "Open Sans", sans-serif; font-weight: 600; font-size: 15px; line-height: 18px;
    color: var(--cyan-deep); text-transform: uppercase; letter-spacing: 1px;
  }
  .tear-off-fields {
    display: flex; gap: 14px; margin-top: 10px;
  }
  .tear-off-field {
    flex: 1; display: flex; align-items: flex-end; gap: 6px;
    font-family: "Open Sans", sans-serif; font-size: 16px; line-height: 20px;
    color: var(--ink);
  }
  .tear-off-field span.line {
    flex: 1; height: 20px; border-bottom: 1.5px solid var(--ink);
  }
</style>
</head>
<body>
  <main class="flyer">
    <div class="trainer-photo" role="img" aria-label="Photo of a smiling female trainer in a pink sports top with arms crossed"></div>
    <div class="slogan-art" role="img" aria-label="Hand-lettered slogan 'yes you can!' beside a pointing fist illustration"></div>

    <h1 class="brand-name">LARKHOLLOW</h1>
    <p class="brand-tagline">PERSONAL TRAINNING</p>

    <section class="headline-band">
      <p>Who else wants to lose at least 15 pounds fast…</p>
      <p>and look and feel better than you have in years?</p>
      <p>These members did…and now you can too!</p>
    </section>

    <h2 class="offer-title">YOUR KICKSTART</h2>
    <ul class="offer-list">
      <li>16 30min Fat-Blasting Training Session with a Larkhollow Personal</li>
      <li>Training Fitness Professional (£347.00 Value)</li>
      <li>4-Weeks of Nutritional Guidnace&nbsp; ($32 Value)</li>
      <li>Unlimited E-mail Coaching (Priceless)</li>
      <li>Done-For-You Meal Plan ($57 Value)</li>
    </ul>

    <section class="tear-off" aria-label="Tear-off details slip">
      <p class="tear-off-title">Tear off &amp; return to claim your kickstart</p>
      <div class="tear-off-fields">
        <div class="tear-off-field">Name<span class="line"></span></div>
        <div class="tear-off-field">Phone<span class="line"></span></div>
        <div class="tear-off-field">Email<span class="line"></span></div>
      </div>
    </section>
  </main>
</body>
</html>
```